BRIGHTDESK - Remote Tech Support Site

We are looking for a new very responsive and simple website for our brand Brightdesk.com - a remote technical support company.

This company supports customers Globally in different countries throughout Eur/ North America / South America / Asia etc (please keep this in mind and integrate into the idea).

Its important to us that the design is very explanatory, the customer should easily be able to figure out that we provide computer support right away ... I like one page responsive type designs as well without a bunch of menu items

Here are some similar sites we like - but still looking for a unique design that fits out brand "brightdesk" - I have upload also some layouts i like (but the designs are not important just the layouts), youll see it includes consumer business etc which is important.

VOLM.COM - I love how clean it is - nice and white easy to see everything

PLUMWIRE247.COM - also nice the layout and responsive one page design makes it easy to use

corvalfix.com - similar to plumwire design as well - you can get the idea im looking for between the two

You will notice those examples are much different then the attachments I added - again this is more of an idea for possible layouts .. attached is also the logo - could inspire color scheme / blue white black etc

Target Market(s)

Home consumers without computer knowledge , older age 45-65, small medium business ... computer repair - slow computers

Industry/Entity Type

Computer Repair

Logo Text

Brightdesk

Coding

Coded - Design and coding required

Number of Pages Required

1 page

Font styles to use
Sans Serif
Other font styles liked:
• your choice responsive

Colors

Designer to choose colors to be used in the design.

Requirements
Must have
• Clean - responsive - professional design - the name says it all - brightdesk
• CALL TO ACTIONS FOR "Get Help Now!" / "Learn More" etc
Nice to have
• We are looking for a new very responsive and simple website for our brand Brightdesk.com - a remote technical support company.
• This company supports customers Globally in different countries throughout Eur/ North America / South America / Asia etc (please keep this in mind and integrate into the idea).
• Its important to us that the design is very explanatory, the customer should easily be able to figure out that we provide computer support right away ... I like one page responsive type designs as well without a bunch of menu items
• Here are some similar sites we like - but still looking for a unique design that fits out brand "brightdesk" - I have upload also some layouts i like (but the designs are not important just the layouts), youll see it includes consumer business etc which is important.
• VOLM.COM - I love how clean it is - nice and white easy to see everything
• PLUMWIRE247.COM - also nice the layout and responsive one page design makes it easy to use
• corvalfix.com - similar to plumwire design as well - you can get the idea im looking for between the two
Should not have
• dark, packed page - bad small font -

```html
<!DOCTYPE html>
<html lang="en">
<head>
<meta charset="utf-8">
<title>Brightdesk – Remote Tech Support</title>
<link href="https://fonts.googleapis.com/css2?family=Montserrat:wght@400;500;600;700;800&family=Open+Sans:wght@400;600;700&display=swap" rel="stylesheet">
<style>
:root{
  --blue:#1e8ff2;
  --blue-dark:#1572cf;
  --blue-deep:#0f5fb0;
  --ink:#2f3338;
  --text:#6a6f75;
  --grey-bg:#e3e4e6;
  --grey-mid:#c9cbce;
  --white:#ffffff;
  --footer:#3b3f46;
  --footer-bar:#2e3137;
  --footer-text:#aeb2b8;
}
*{box-sizing:border-box;margin:0;padding:0}
html,body{width:1200px;height:4327px;overflow:hidden}
body{font-family:"Open Sans",Arial,sans-serif;color:var(--text);background:var(--white);position:relative}
section,header,footer{position:absolute;left:0;width:1200px}
.abs{position:absolute}
h1,h2,h3,h4{font-family:"Montserrat",Arial,sans-serif}
.btn{display:inline-block;font-family:"Montserrat",Arial,sans-serif;font-weight:700;font-size:12px;letter-spacing:.5px;text-transform:uppercase;border-radius:4px;padding:13px 26px;text-align:center}
.btn-white{background:var(--white);color:var(--blue)}
.btn-blue{background:var(--blue);color:var(--white)}

/* header */
.site-header{top:0;height:86px;z-index:5}
.logo{left:88px;top:24px;display:flex;align-items:center;gap:10px;color:var(--white);font-family:"Montserrat",sans-serif;font-weight:600;font-size:26px}
.logo-dot{width:34px;height:34px;border-radius:50%;background:var(--white)}
.nav{left:354px;top:36px;display:flex;gap:30px;font-family:"Montserrat",sans-serif;font-size:13px;font-weight:600;color:var(--white)}
.search-btn{left:848px;top:28px;width:34px;height:34px;background:var(--blue);border-radius:3px}
.callout{left:760px;top:64px;width:170px;background:var(--blue-deep);color:var(--white);font-size:10px;line-height:13px;text-align:center;padding:6px 6px;border-radius:3px}
.callout b{display:block;font-size:13px;font-family:"Montserrat",sans-serif;margin-top:2px}
.mail{left:912px;top:34px}
.lang{left:970px;top:36px;color:var(--white);font-size:12px;font-weight:700;display:flex;gap:6px;align-items:center}
.lang i{width:16px;height:11px;background:var(--white);opacity:.7;display:block}
.login{left:1030px;top:28px;background:var(--white);color:var(--blue);font-family:"Montserrat",sans-serif;font-weight:700;font-size:12px;padding:9px 18px;border-radius:4px;display:flex;gap:8px;align-items:center}

/* hero */
.hero{top:0;height:554px;background:linear-gradient(90deg,#1b8bf0 0%,#2a95f2 45%,#6aa8d9 65%,#cdd6df 100%);overflow:hidden}
.hero-photo{left:560px;top:0;width:640px;height:554px;background:linear-gradient(90deg,rgba(40,146,240,0) 0%,#bcc9d6 35%,#dfe3e8 70%,#eef0f2 100%)}
.hero h1{left:88px;top:214px;width:560px;color:var(--white);font-size:40px;line-height:50px;font-weight:700}
.hero .lead{left:88px;top:326px;color:var(--white);font-size:17px}
.hero .btn{left:88px;top:364px}
.hero .member{left:88px;top:428px;color:var(--white);font-size:13px}
.hero .member b{font-weight:700}
.dots{left:572px;top:492px;display:flex;gap:8px}
.dots i{width:12px;height:12px;border-radius:50%;background:rgba(255,255,255,.55);display:block}
.dots i:first-child{background:var(--white)}

/* trust */
.trust{top:554px;height:211px;background:var(--white)}
.trust h2{top:42px;width:1200px;text-align:center;color:var(--blue);font-size:22px;font-weight:700}
.press{left:385px;top:110px;width:440px;display:grid;grid-template-columns:repeat(5,1fr);gap:18px 22px}
.press span{height:18px;background:#cfd2d6;border-radius:2px;display:block}

/* problems */
.problems{top:765px;height:533px;background:#dcdee1}
.problems-photo{left:0;top:0;width:592px;height:533px;background:linear-gradient(135deg,#eef0f2 0%,#d6dadf 55%,#b9c0c8 100%)}
.problems h2{left:615px;top:46px;font-size:27px;color:var(--ink);font-weight:600}
.problems .intro{left:615px;top:96px;width:340px;font-size:15px;line-height:22px;color:var(--text)}
.call-btn{left:615px;top:150px;background:var(--blue);color:var(--white);font-size:20px;font-family:"Montserrat",sans-serif;padding:15px 24px;border-radius:4px}
.problems .or{left:615px;top:225px;font-size:16px}
.field{left:615px;width:335px;height:30px;background:var(--white);border-radius:3px;font-size:10px;color:#999;padding:9px 10px}
.pref{left:615px;top:395px;font-size:15px}
.slots{left:615px;top:425px;display:flex;gap:18px;font-size:13px}
.slots label{display:flex;align-items:center;gap:6px}
.box{width:22px;height:22px;background:var(--white);border:1px solid #bbb}
.problems .btn{left:615px;top:460px;padding:11px 20px}

/* how */
.how{top:1298px;height:303px;background:var(--blue)}
.how h2{top:42px;width:1200px;text-align:center;color:var(--white);font-size:20px;font-weight:700}
.steps{left:270px;top:92px;width:660px;display:grid;grid-template-columns:repeat(3,1fr);gap:40px;text-align:center;color:var(--white)}
.steps h3{font-size:14px;font-weight:600;margin:14px 0 8px}
.steps p{font-size:13px;line-height:18px;color:#e3f0fd}

/* pricing */
.pricing{top:1601px;height:482px;background:linear-gradient(90deg,#dcdfe3 0%,#eef0f2 20%,#f3f4f5 50%,#eef0f2 80%,#d6dade 100%)}
.pricing h2{top:42px;width:1200px;text-align:center;color:var(--blue);font-size:20px;font-weight:700}
.plans{left:243px;top:95px;display:flex;align-items:flex-start}
.plan{width:240px;background:#f6f6f6;text-align:center;border:1px solid #d8d8d8}
.plan-head{background:#d9dadc;font-family:"Montserrat",sans-serif;font-weight:700;font-size:13px;color:var(--ink);padding:12px}
.price{font-family:"Montserrat",sans-serif;font-size:44px;font-weight:600;color:var(--ink);margin-top:22px}
.price sup{font-size:22px}
.price small{font-size:13px;color:var(--blue);font-weight:400}
.setup{font-size:11px;color:var(--blue);margin-top:2px}
.plan .desc{font-size:12px;color:var(--text);margin-top:28px;line-height:17px}
.plan .desc b{display:block;color:var(--ink);font-size:14px}
.plan .btn{margin:24px 0 24px;padding:11px 20px}
.plan.featured{width:285px;background:var(--blue);border:0;margin-top:-22px;color:var(--white)}
.plan.featured .plan-head{background:var(--blue-dark);color:var(--white)}
.plan.featured .price,.plan.featured .desc b{color:var(--white)}
.plan.featured .price{background:var(--white);color:var(--blue);margin:22px 24px 0;padding:4px 0;border-radius:3px}
.plan.featured .setup,.plan.featured .desc{color:#e4f1fe}
.plan.featured .price small{color:var(--blue)}
.offer{left:285px;top:422px;font-size:15px;display:flex;gap:10px;align-items:center;color:var(--text)}
.offer b{color:var(--ink)}

/* features */
.features{top:2083px;height:340px;background:var(--white)}
.features h2{top:44px;width:1200px;text-align:center;color:var(--blue);font-size:20px;font-weight:700}
.feat-grid{left:180px;top:105px;width:850px;display:grid;grid-template-columns:1fr 1fr;gap:44px 70px}
.feat{display:flex;gap:22px}
.feat h3{font-size:17px;font-weight:600;color:var(--blue);margin-bottom:4px}
.feat p{font-size:15px;line-height:21px;color:var(--text)}
.feat svg{flex:none}
.features-more{top:2423px;height:341px;background:var(--grey-bg)}
.features-more .feat-grid{top:44px}
.features-more .feat h3{color:var(--ink)}
.features-more .btn{left:546px;top:270px;padding:11px 22px}

/* realtime */
.realtime{top:2764px;height:438px;background:var(--blue);overflow:hidden}
.realtime-photo{left:600px;top:0;width:600px;height:438px;background:linear-gradient(90deg,rgba(30,143,242,1) 0%,#9cc3e6 35%,#e8e3d4 70%,#f1ede2 100%)}
.realtime h2{left:160px;top:40px;width:440px;color:var(--white);font-size:37px;line-height:46px;font-weight:500}
.realtime h2 b{font-weight:700}
.ticks{left:160px;top:150px;list-style:none;color:var(--white);font-size:15px}
.ticks li{display:flex;gap:12px;align-items:center;margin-bottom:19px}
.realtime .btn{left:160px;top:330px;padding:11px 18px;font-size:11px}

/* join */
.join{top:3202px;height:260px;background:linear-gradient(180deg,#f5f6f7 0%,#e7e9ec 100%);text-align:center}
.join h2{top:34px;width:1200px;color:var(--blue);font-size:38px;font-weight:700}
.join .from{top:100px;width:1200px;font-size:29px;color:var(--text);font-family:"Montserrat",sans-serif}
.join .amount{top:140px;width:1200px;font-size:40px;font-weight:700;color:var(--ink);font-family:"Montserrat",sans-serif}
.join .amount small{font-size:18px;color:var(--blue);font-weight:400}
.join .btn{left:543px;top:198px;padding:11px 24px}

/* call */
.call{top:3462px;height:389px;background:var(--white)}
.call h2{top:44px;width:1200px;text-align:center;color:var(--ink);font-size:18px;font-weight:800}
.call .sub{top:72px;width:1200px;text-align:center;font-size:17px;color:var(--text)}
.call-box{left:88px;top:130px;width:1022px;height:303px;display:flex;z-index:3}
.video{width:567px;height:303px;position:relative;background:linear-gradient(135deg,#e5ecf3 0%,#cfdbe8 60%,#b7c7d8 100%)}
.video-bar{position:absolute;left:0;bottom:0;width:100%;height:36px;background:#222;display:flex;align-items:center;gap:10px;padding:0 14px}
.video-bar .track{flex:1;height:4px;background:#666}
.consult{flex:1;background:var(--blue);color:var(--white);padding:70px 40px;text-align:center}
.consult h3{font-size:27px;line-height:34px;font-weight:700}
.consult .btn{margin-top:22px;padding:11px 22px;font-size:11px}

/* footer */
.site-footer{top:3851px;height:425px;background:var(--footer);color:var(--footer-text)}
.f-logo{left:88px;top:88px;display:flex;align-items:center;gap:9px;color:var(--white);font-family:"Montserrat",sans-serif;font-size:25px;font-weight:600}
.f-logo i{width:30px;height:30px;border-radius:50%;border:3px solid var(--white);display:block}
.contact{left:88px;top:138px;font-size:15px;color:var(--white)}
.contact div{display:flex;gap:10px;align-items:center;margin-bottom:10px}
.contact .mail-link{color:#6db8ff}
.about{left:88px;top:210px;width:250px;font-size:11px;line-height:16px}
.about p+p{margin-top:12px}
.col{top:100px;font-size:11px;line-height:19px}
.col h4{color:var(--white);font-size:16px;font-weight:700;margin-bottom:12px}
.follow{left:408px;top:292px}
.follow h4{color:var(--white);font-size:16px;font-weight:700;margin-bottom:12px}
.socials{display:flex;gap:10px}
.socials i{width:32px;height:32px;border-radius:50%;background:var(--blue);display:block}
.newsletter{left:878px;top:100px;width:238px}
.newsletter h4{color:var(--white);font-size:16px;font-weight:700;margin-bottom:10px}
.newsletter p{font-size:10px;margin-bottom:8px}
.newsletter .input{height:26px;background:var(--white);border-radius:2px;font-size:10px;color:#999;padding:6px 8px}
.newsletter .btn{margin-top:10px;padding:8px 16px;font-size:10px}
.trusted{left:705px;top:292px}
.trusted h4{color:var(--white);font-size:16px;font-weight:700;margin-bottom:10px}
.badges{display:flex;gap:12px;align-items:center}
.badges .round{width:50px;height:50px;border-radius:50%;background:#c89b2e}
.badges .seal{width:50px;height:50px;border-radius:50%;background:#b23a2e}
.badges .rect{width:90px;height:36px;background:#e9eaeb;border-radius:2px}
.footer-bar{top:4276px;height:51px;background:var(--footer-bar);color:var(--footer-text);font-size:11px;padding:18px 88px}
</style>
</head>
<body>

<section class="hero">
  <div class="abs hero-photo" role="img" aria-label="Photo of an older couple smiling at a laptop together"></div>
  <h1 class="abs">It has never been easier to get PC &amp; Internet help...</h1>
  <p class="abs lead">More than tech support. People Support.</p>
  <a class="abs btn btn-white">Learn More</a>
  <p class="abs member">Already a member? <b>CLICK HERE</b> to get help</p>
  <div class="abs dots"><i></i><i></i><i></i></div>
</section>

<header class="site-header">
  <div class="abs logo"><span class="logo-dot"></span>brightdesk</div>
  <nav class="abs nav"><span>Home</span><span>About Us</span><span>Services</span><span>Contact Us</span><span>Shop</span></nav>
  <div class="abs search-btn">
    <svg width="34" height="34" viewBox="0 0 34 34"><circle cx="15" cy="15" r="6" fill="none" stroke="#fff" stroke-width="2"/><line x1="19.5" y1="19.5" x2="24" y2="24" stroke="#fff" stroke-width="2"/></svg>
  </div>
  <div class="abs callout">Call now and let our IT experts give your PC a FREE healthcheck!<b>(800) 0412-775</b></div>
  <svg class="abs mail" width="24" height="18" viewBox="0 0 24 18"><rect x="1" y="1" width="22" height="16" fill="none" stroke="#fff" stroke-width="2"/><polyline points="1,1 12,10 23,1" fill="none" stroke="#fff" stroke-width="2"/></svg>
  <div class="abs lang">EN <i></i></div>
  <div class="abs login">LOGIN
    <svg width="14" height="14" viewBox="0 0 14 14"><circle cx="7" cy="7" r="6" fill="none" stroke="#1e8ff2" stroke-width="1.5"/><polyline points="6,4 9,7 6,10" fill="none" stroke="#1e8ff2" stroke-width="1.5"/></svg>
  </div>
</header>

<section class="trust">
  <h2 class="abs">Volm is the most trusted home tech services company</h2>
  <div class="abs press"><span></span><span></span><span></span><span></span><span></span><span></span><span></span><span></span><span></span><span></span></div>
</section>

<section class="problems">
  <div class="abs problems-photo" role="img" aria-label="Photo of friendly support agents with headsets working at computers"></div>
  <h2 class="abs">Problems with your PC ?</h2>
  <p class="abs intro">One of our friendly IT experts can give your computer a FREE healthcheck today!</p>
  <a class="abs call-btn">CALL +1 866 418 2260</a>
  <p class="abs or">Or book a time here:</p>
  <div class="abs field" style="top:255px">Your Name</div>
  <div class="abs field" style="top:295px">Your Email</div>
  <div class="abs field" style="top:335px">Telephone Number</div>
  <p class="abs pref">Preferred time of day for us to contact you</p>
  <div class="abs slots">
    <label><svg width="22" height="22" viewBox="0 0 22 22"><polyline points="4,11 9,16 18,5" fill="none" stroke="#1e8ff2" stroke-width="3"/></svg>08:00 - 11:00</label>
    <label><span class="box"></span>08:00 - 11:00</label>
    <label><span class="box"></span>08:00 - 11:00</label>
  </div>
  <a class="abs btn btn-blue">Learn More</a>
</section>

<section class="how">
  <h2 class="abs">How It Works</h2>
  <div class="abs steps">
    <div>
      <svg width="44" height="40" viewBox="0 0 44 40"><rect x="4" y="8" width="36" height="24" rx="3" fill="none" stroke="#fff" stroke-width="2.5"/><line x1="4" y1="24" x2="40" y2="24" stroke="#fff" stroke-width="2"/></svg>
      <h3>FREE Diagnostic</h3>
      <p>Get a diagnostic, FOR FREE! Get a free consultation with our staff.</p>
    </div>
    <div>
      <svg width="44" height="40" viewBox="0 0 44 40"><line x1="8" y1="6" x2="36" y2="34" stroke="#fff" stroke-width="3"/><line x1="36" y1="6" x2="8" y2="34" stroke="#fff" stroke-width="3"/><circle cx="8" cy="6" r="4" fill="none" stroke="#fff" stroke-width="2"/></svg>
      <h3>Get Fixed</h3>
      <p>Get fixed, IMMEDIATELY! Our staff will solve your computer issues right before your eyes.</p>
    </div>
    <div>
      <svg width="44" height="40" viewBox="0 0 44 40"><path d="M8 22 Q20 6 36 12" fill="none" stroke="#fff" stroke-width="3"/><polyline points="8,12 8,22 18,22" fill="none" stroke="#fff" stroke-width="3"/></svg>
      <h3>Backup your information!</h3>
      <p>Saving your files is now EASY! You will be able to retain your personal files without any loss of data.</p>
    </div>
  </div>
</section>

<section class="pricing">
  <div class="abs" style="left:0;top:0;width:1200px;height:482px" role="img" aria-label="Background photo of two happy customers at their computers"></div>
  <h2 class="abs">Membership Pricing and Plans</h2>
  <div class="abs plans">
    <div class="plan">
      <div class="plan-head">PREMIUM</div>
      <div class="price"><sup>$</sup>19.99 <small>/ month</small></div>
      <div class="setup">($249 $300 setup fee)</div>
      <div class="desc">Regular 90-Day Optimization<b>Unlimited 24/7 Tier 3<br>Technician Support</b></div>
      <a class="btn btn-blue">Learn More</a>
    </div>
    <div class="plan">
      <div class="plan-head">PREMIUM PLUS</div>
      <div class="price"><sup>$</sup>29.99 <small>/ month</small></div>
      <div class="setup">($249 $300 setup fee)</div>
      <div class="desc">Regular 90-Day Optimization<b>Unlimited 24/7 Tier 3<br>Technician Support</b></div>
      <a class="btn btn-blue">Learn More</a>
    </div>
    <div class="plan featured">
      <div class="plan-head">PREMIUM</div>
      <div class="price"><sup>$</sup>39.99 <small>/ month</small></div>
      <div class="setup">($249 $300 setup fee)</div>
      <div class="desc">Regular 90-Day Optimization<b>Unlimited 24/7 Tier 3<br>Technician Support</b></div>
      <a class="btn btn-white">Learn More</a>
    </div>
  </div>
  <p class="abs offer"><svg width="20" height="16" viewBox="0 0 20 16"><polyline points="2,8 7,13 18,2" fill="none" stroke="#1e8ff2" stroke-width="3"/></svg><span><b>FREE</b> Optimization and Diagnostic when you call in. Limited time offer.</span></p>
</section>

<section class="features">
  <h2 class="abs">All The Best Features, At The Best Price!</h2>
  <div class="abs feat-grid">
    <div class="feat">
      <svg width="100" height="64" viewBox="0 0 100 64"><rect x="10" y="4" width="80" height="48" rx="3" fill="none" stroke="#1e8ff2" stroke-width="3"/><line x1="2" y1="58" x2="98" y2="58" stroke="#1e8ff2" stroke-width="3"/><text x="50" y="34" text-anchor="middle" font-size="14" font-family="Montserrat" font-weight="700" fill="#1e8ff2">www</text></svg>
      <div><h3>Ad Blocker</h3><p>Avoid unwanted Pop-ups with the newest Ad Blocking technology.</p></div>
    </div>
    <div class="feat">
      <svg width="100" height="64" viewBox="0 0 100 64"><rect x="10" y="4" width="80" height="48" rx="3" fill="none" stroke="#1e8ff2" stroke-width="3"/><line x1="2" y1="58" x2="98" y2="58" stroke="#1e8ff2" stroke-width="3"/><polyline points="22,40 40,28 54,34 76,16" fill="none" stroke="#1e8ff2" stroke-width="3"/></svg>
      <div><h3>Regular Tune-Ups</h3><p>Get a Regular Tune-Up and Optimization every 90 days.</p></div>
    </div>
    <div class="feat">
      <svg width="100" height="64" viewBox="0 0 100 64"><rect x="10" y="4" width="80" height="52" rx="3" fill="none" stroke="#1e8ff2" stroke-width="3"/><line x1="10" y1="14" x2="90" y2="14" stroke="#1e8ff2" stroke-width="3"/><rect x="20" y="22" width="22" height="24" fill="none" stroke="#1e8ff2" stroke-width="2"/><line x1="50" y1="26" x2="80" y2="26" stroke="#1e8ff2" stroke-width="2"/><line x1="50" y1="34" x2="80" y2="34" stroke="#1e8ff2" stroke-width="2"/><line x1="50" y1="42" x2="72" y2="42" stroke="#1e8ff2" stroke-width="2"/></svg>
      <div><h3>System Reports</h3><p>Stay up to date with Real-Time System Reporting.</p></div>
    </div>
    <div class="feat">
      <svg width="100" height="64" viewBox="0 0 100 64"><rect x="18" y="4" width="64" height="40" rx="3" fill="none" stroke="#1e8ff2" stroke-width="3"/><rect x="4" y="26" width="22" height="34" rx="3" fill="#fff" stroke="#1e8ff2" stroke-width="3"/><rect x="68" y="30" width="28" height="30" rx="3" fill="#fff" stroke="#1e8ff2" stroke-width="3"/></svg>
      <div><h3>Multiple Devices</h3><p>Get support for up to 4 multiple devices. Ask about our Family Plans.</p></div>
    </div>
  </div>
</section>

<section class="features-more">
  <div class="abs feat-grid">
    <div class="feat">
      <svg width="100" height="64" viewBox="0 0 100 64"><rect x="10" y="4" width="80" height="52" rx="3" fill="none" stroke="#fff" stroke-width="3"/><line x1="10" y1="14" x2="90" y2="14" stroke="#fff" stroke-width="3"/><line x1="22" y1="28" x2="78" y2="28" stroke="#fff" stroke-width="2"/><line x1="22" y1="38" x2="78" y2="38" stroke="#fff" stroke-width="2"/></svg>
      <div><h3>Identity Protection</h3><p>Coming Soon</p></div>
    </div>
    <div class="feat">
      <svg width="100" height="64" viewBox="0 0 100 64"><rect x="36" y="2" width="28" height="56" rx="4" fill="none" stroke="#fff" stroke-width="3"/><path d="M24 18 Q18 30 24 42 M76 18 Q82 30 76 42" fill="none" stroke="#fff" stroke-width="3"/></svg>
      <div><h3>Mobile Security</h3><p>Coming Soon</p></div>
    </div>
    <div class="feat">
      <svg width="100" height="64" viewBox="0 0 100 64"><rect x="30" y="2" width="40" height="58" rx="4" fill="none" stroke="#fff" stroke-width="3"/><path d="M20 50 L40 30 L50 40" fill="none" stroke="#fff" stroke-width="3"/></svg>
      <div><h3>Cross Platform Support</h3><p>One Support Plan for different types of devices.</p></div>
    </div>
    <div class="feat">
      <svg width="100" height="64" viewBox="0 0 100 64"><path d="M26 46 Q10 46 12 32 Q14 20 28 22 Q34 6 52 8 Q70 10 72 24 Q90 24 88 38 Q86 46 74 46" fill="none" stroke="#fff" stroke-width="3"/><line x1="50" y1="30" x2="50" y2="60" stroke="#fff" stroke-width="3"/><polyline points="42,52 50,60 58,52" fill="none" stroke="#fff" stroke-width="3"/></svg>
      <div><h3>Cloud Backup</h3><p>Keep your data safe! Ask about our plans for Unlimited Cloud Backup.</p></div>
    </div>
  </div>
  <a class="abs btn btn-blue">Learn More</a>
</section>

<section class="realtime">
  <div class="abs realtime-photo" role="img" aria-label="Photo of a smiling woman using her laptop"></div>
  <h2 class="abs">Real-Time Support Features and <b>Benefits</b></h2>
  <ul class="abs ticks">
    <li><svg width="18" height="14" viewBox="0 0 18 14"><polyline points="1,7 6,12 17,1" fill="none" stroke="#fff" stroke-width="3"/></svg>24/7 Real-Time Technician Support</li>
    <li><svg width="18" height="14" viewBox="0 0 18 14"><polyline points="1,7 6,12 17,1" fill="none" stroke="#fff" stroke-width="3"/></svg>The best Security Software in the market</li>
    <li><svg width="18" height="14" viewBox="0 0 18 14"><polyline points="1,7 6,12 17,1" fill="none" stroke="#fff" stroke-width="3"/></svg>Regular tune-ups and optimization</li>
    <li><svg width="18" height="14" viewBox="0 0 18 14"><polyline points="1,7 6,12 17,1" fill="none" stroke="#fff" stroke-width="3"/></svg>Setup and installation included</li>
  </ul>
  <a class="abs btn btn-white">Become a Member</a>
</section>

<section class="join" role="img" aria-label="Faint background photo of a computer keyboard">
  <h2 class="abs">Become a Member Today!</h2>
  <p class="abs from">Starting At Only</p>
  <p class="abs amount">$19.99 <small>/ month</small></p>
  <a class="abs btn btn-blue">Get Started</a>
</section>

<section class="call">
  <h2 class="abs">CALL US TODAY</h2>
  <p class="abs sub">And get started with our dedicated technicians.</p>
  <div class="abs call-box">
    <div class="video" role="img" aria-label="Illustrated video of a support technician helping a customer at a computer">
      <div class="video-bar">
        <svg width="14" height="16" viewBox="0 0 14 16"><polygon points="1,1 13,8 1,15" fill="#fff"/></svg>
        <span class="track"></span>
        <svg width="18" height="14" viewBox="0 0 18 14"><rect x="1" y="1" width="16" height="12" fill="none" stroke="#fff" stroke-width="2"/></svg>
      </div>
    </div>
    <div class="consult">
      <h3>Get a 30-minute one-on-one free consultation with one of our experts! *</h3>
      <a class="btn btn-white">Limited Period Offer</a>
    </div>
  </div>
</section>

<footer class="site-footer">
  <div class="abs f-logo"><i></i>brightdesk</div>
  <div class="abs contact">
    <div><svg width="16" height="16" viewBox="0 0 16 16"><path d="M3 1 L6 1 L7 5 L5 6 Q6 9 10 11 L11 9 L15 10 L15 13 Q14 15 12 15 Q3 13 1 4 Q1 2 3 1Z" fill="#fff"/></svg>(800) 0412-775</div>
    <div class="mail-link"><svg width="16" height="12" viewBox="0 0 16 12"><rect x="1" y="1" width="14" height="10" fill="none" stroke="#6db8ff" stroke-width="1.6"/><polyline points="1,1 8,7 15,1" fill="none" stroke="#6db8ff" stroke-width="1.6"/></svg>info@brightdesk.com</div>
  </div>
  <div class="abs about">
    <p>We are a group of technicians who work round the clock to ensure that your PC works perfectly. Get your computer free of suspicious software and have a healthy system.</p>
    <p>You can get in touch with us any time of the day, any day of the week. We offer support through phone and online chat.</p>
  </div>
  <div class="abs col" style="left:408px"><h4>LINK</h4>Home<br>About Us<br>Services<br>Contact Us<br>FAQs</div>
  <div class="abs col" style="left:545px"><h4>SERVICES</h4>Plans<br>Plans<br>Plans<br>Plans<br>Plans</div>
  <div class="abs col" style="left:705px"><h4>PLANS</h4>Premium Plan<br>Premium Plus Plan<br>Platinum Plan</div>
  <div class="abs newsletter">
    <h4>NEWSLETTER</h4>
    <p>Sign up for our regular informational newsletter.</p>
    <div class="input">Email</div>
    <a class="btn btn-blue">Sign Up</a>
  </div>
  <div class="abs follow"><h4>FOLLOW US</h4><div class="socials"><i></i><i></i><i></i></div></div>
  <div class="abs trusted"><h4>TRUSTED BY</h4><div class="badges"><span class="round"></span><span class="seal"></span><span class="rect"></span></div></div>
</footer>
<div class="abs footer-bar" style="position:absolute;left:0;width:1200px">Brightdesk © 2017. All rights reserved. Terms and Conditions · Privacy Policy</div>

</body>
</html>
```